ORVILMA card Technical Architecture

Hello everyone ORVILMA: It is a consulting firm in Architecture and Construction. I require a card duplexing, sober, elegant, classic but not boring. Update 1: Use the following data for the card. Name: Rodrigo Salinas Tomás Quevedo Position: COO Twitter: @orvilmaAT Homepage: orvilma.com home address not include the participation of all thank you.

Target Market(s)

Construction companies, Architects and Consulting Engineers

Industry/Entity Type

Consulting

Contact Information for Business Card

Los campos que debe tener:
Nombre, Cargo, email, homepage y twitter

Font styles to use
Serif
Sans Serif
Other font styles liked:
• Me gustan playfair display, open sans y roboto, pero estoy sujeto a sus propuestas

Requirements
Must have
• Colors: Present combined proposals in white, red, gray and black Update 1: The two names must be clearly differentiated from the two surnames
Nice to have
• They are free to present their best proposals. I will bring them immediate feedback to the extent you can go see their designs. Complete data for card and logo files will give the winner the

```html
<!DOCTYPE html>
<html lang="es">
<head>
<meta charset="utf-8">
<title>ORVILMA — Tarjetas de presentación</title>
<link rel="stylesheet" href="https://fonts.googleapis.com/css2?family=Open+Sans:wght@300;400;600&display=swap">
<style>
  :root {
    --backdrop: #54473c;
    --paper: #ffffff;
    --ink: #1a1a1a;
    --muted: #5a5a5a;
    --brand-red: #9b0a0e;
    --red-light: #c2030b;
    --red-dark: #6a0003;
    --black: #000000;
    --slate: #1f2427;
    --rule: #cfcfcf;
  }
  * { box-sizing: border-box; margin: 0; padding: 0; }
  html, body {
    width: 1200px; height: 777px; overflow: hidden;
    background: var(--backdrop);
    font-family: "Open Sans", Arial, sans-serif;
  }
  .sheet { position: relative; width: 1200px; height: 777px; }
  .card {
    position: absolute; width: 485px; height: 277px; overflow: hidden;
  }
  .card--front { left: 100px; top: 97px; background: var(--paper); }
  .card--black { left: 616px; top: 97px; background: var(--black); }
  .card--red {
    left: 100px; top: 400px;
    background: radial-gradient(ellipse 60% 75% at 45% 45%, var(--red-light) 0%, #950006 55%, var(--red-dark) 100%);
  }
  .card--slate { left: 616px; top: 400px; background: var(--slate); }

  /* Front */
  .brand {
    position: absolute; left: 52px; top: 134px; width: 178px; text-align: center;
  }
  .brand__name {
    font-weight: 400; font-size: 26px; letter-spacing: 6px; color: var(--ink);
    line-height: 1; padding-left: 6px;
  }
  .brand__tagline {
    margin-top: 6px; padding-top: 4px; border-top: 1px solid #b9b9b9;
    font-size: 8.5px; letter-spacing: 2.4px; color: var(--brand-red);
    text-transform: uppercase;
  }
  .divider {
    position: absolute; left: 256px; top: 69px; width: 1px; height: 139px;
    background: var(--rule);
  }
  .person { position: absolute; left: 278px; top: 75px; }
  .person__name {
    font-weight: 600; font-size: 17.5px; line-height: 21px; color: var(--brand-red);
  }
  .person__role { font-size: 12.5px; color: var(--ink); margin-top: 2px; }
  .contacts { list-style: none; margin-top: 13px; }
  .contacts li {
    display: flex; align-items: center; gap: 7px;
    font-size: 12.5px; line-height: 18.5px; color: var(--muted);
  }
  .contacts svg { width: 11px; height: 11px; flex: none; }

  /* Backs */
  .back__name {
    position: absolute; left: 0; right: 0; top: 100px; text-align: center;
    font-weight: 300; font-size: 46px; letter-spacing: 12px; padding-left: 12px;
    color: #ffffff; line-height: 1;
  }
  .back__url {
    position: absolute; left: 0; right: 0; top: 233px; text-align: center;
    font-size: 13.5px; letter-spacing: 9px; padding-left: 9px; color: #ffffff;
  }
</style>
</head>
<body>
<main class="sheet">

  <section class="card card--front" aria-label="Anverso">
    <div class="brand">
      <p class="brand__name">ORVILMA</p>
      <p class="brand__tagline">Arquitectura Técnica</p>
    </div>
    <div class="divider"></div>
    <div class="person">
      <h1 class="person__name">Rodrigo Salinas<br>Tomás Quevedo</h1>
      <p class="person__role">Director de Operaciones</p>
      <ul class="contacts">
        <li>
          <svg viewBox="0 0 12 12" aria-hidden="true"><path fill="#9b0a0e" d="M2.6 0.6l1.9 2.2-1 1.3c.6 1.6 1.8 2.8 3.4 3.4l1.3-1 2.2 1.9-.9 2.2C5.1 10.7 1.3 6.9.5 1.5z"/></svg>
          (+571) 555 010 2030
        </li>
        <li>
          <svg viewBox="0 0 12 12" aria-hidden="true"><circle cx="6" cy="6" r="5" fill="#9b0a0e"/></svg>
          @orvilmaAT
        </li>
        <li>
          <svg viewBox="0 0 12 12" aria-hidden="true"><circle cx="6" cy="6" r="5.2" fill="#9b0a0e"/><path d="M1 6h10M6 1c-2.2 2.8-2.2 7.2 0 10M6 1c2.2 2.8 2.2 7.2 0 10" stroke="#fff" stroke-width=".8" fill="none"/></svg>
          www.orvilma.com
        </li>
      </ul>
    </div>
  </section>

  <section class="card card--black" aria-label="Reverso negro">
    <p class="back__name">ORVILMA</p>
    <p class="back__url">www.orvilma.com</p>
  </section>

  <section class="card card--red" aria-label="Reverso rojo">
    <p class="back__name">ORVILMA</p>
    <p class="back__url">www.orvilma.com</p>
  </section>

  <section class="card card--slate" aria-label="Reverso gris">
    <p class="back__name">ORVILMA</p>
    <p class="back__url">www.orvilma.com</p>
  </section>

</main>
</body>
</html>
```